KickTime Lots iPhone App Splash Page and Company Logo

KickTime Lots has developed several iPhone applications to help college football (American football, not European football/soccer) fans find parking on game days. The current logo and several splash pages are included here.

We are looking for an updated/fresh logo for our new "universal" app - a single iPhone app that provides information for all college football venues (currently there is a separate app for each venue). Specifically, we need an iPhone splash page design that allows space for several (3) buttons on the right side of the splash screen (much like the placement of the buttons on the current splash screens shown). We also need a logo that can work as an iPhone app icon.

The theme should reflect college football, parking, and efficiency.

Target Market(s)

College graduates attending saturday football games.

Industry/Entity Type

College

Logo Text

College Football KickTime Lots

Requirements
Must have
• Clean. Simple. Collegiate feel.

```html
<!DOCTYPE html>
<html lang="en">
<head>
<meta charset="utf-8">
<title>KickTime Lots — Splash Screen</title>
<link rel="stylesheet" href="https://fonts.googleapis.com/css2?family=Oswald:wght@700&display=swap">
<style>
  :root {
    --canvas-bg: #e9ecea;
    --screen-top: #153a33;
    --screen-mid: #1a403a;
    --stand-haze: #2f4e4a;
    --field-light: #4c7a56;
    --field-dark: #335a3e;
    --crowd-mid: #24332f;
    --crowd-dark: #121c1a;
    --brand-green: #20a862;
    --brand-white: #ffffff;
    --brand-navy: #1c2b4a;
  }
  * { margin: 0; padding: 0; box-sizing: border-box; }
  html, body {
    width: 1200px;
    height: 899px;
    overflow: hidden;
    background: var(--canvas-bg);
  }
  .splash-screen {
    position: absolute;
    left: 317px;
    top: 0;
    width: 566px;
    height: 899px;
    overflow: hidden;
    background: linear-gradient(180deg, var(--screen-top) 0%, var(--screen-mid) 35%, var(--crowd-dark) 100%);
    font-family: "Oswald", "Arial Narrow", sans-serif;
  }
  .stadium-photo {
    position: absolute;
    left: 0;
    top: 280px;
    width: 100%;
    height: 619px;
    background:
      radial-gradient(ellipse 60% 18% at 50% 36%, rgba(120,170,130,0.35), rgba(120,170,130,0) 70%),
      linear-gradient(180deg,
        rgba(26,64,58,1) 0%,
        var(--stand-haze) 12%,
        #3a5b55 20%,
        var(--field-dark) 24%,
        var(--field-light) 32%,
        var(--field-light) 38%,
        var(--field-dark) 44%,
        #2a3d39 50%,
        var(--crowd-mid) 62%,
        #1a2624 80%,
        var(--crowd-dark) 100%);
  }
  .brand-badge {
    position: absolute;
    left: 149px;
    top: 46px;
    width: 268px;
    height: 268px;
    border-radius: 50%;
    background: var(--brand-white);
    border: 14px solid var(--brand-green);
    display: flex;
    align-items: center;
    justify-content: center;
  }
  .brand-name {
    color: var(--brand-navy);
    font-weight: 700;
    font-size: 48px;
    line-height: 1.05;
    letter-spacing: 3px;
    text-transform: uppercase;
    text-align: center;
  }
  .headline {
    position: absolute;
    bottom: 92px;
    writing-mode: vertical-rl;
    transform: rotate(180deg);
    font-weight: 700;
    line-height: 1;
    text-transform: uppercase;
  }
  .headline-college {
    left: 96px;
    font-size: 64px;
    letter-spacing: 5px;
    color: var(--brand-white);
  }
  .headline-football {
    left: 176px;
    font-size: 66px;
    letter-spacing: 5px;
    color: var(--brand-green);
  }
</style>
</head>
<body>
  <main class="splash-screen">
    <div class="stadium-photo" role="img" aria-label="Photo of a college football stadium at dusk, with the lit field and a packed crowd in the stands"></div>
    <div class="brand-badge">
      <span class="brand-name">KickTime<br>Lots</span>
    </div>
    <h1>
      <span class="headline headline-college">College</span>
      <span class="headline headline-football">Football</span>
    </h1>
  </main>
</body>
</html>
```